Halverton Construction And Masonry Ltd

Black background

Logo - attached

Services (bullet points)
New Builds
Extensions
Refurbishments
Alterations
Brickwork Specialists

Contact details - 01632 960481 or 0770 0900517

Email address - contact@halvertonconstructionandmasonry.co.uk

Website - www.halvertonconstructionandmasonry.co.uk

Facebook logo

```html
<!DOCTYPE html>
<html lang="en">
<head>
<meta charset="utf-8">
<title>Halverton Construction And Masonry Ltd – Flyer</title>
<link rel="stylesheet" href="https://fonts.googleapis.com/css2?family=Outfit:wght@400;500;600&display=swap">
<style>
  :root {
    --ink: #050505;
    --green: #3fba68;
    --white: #ffffff;
  }
  * { margin: 0; padding: 0; box-sizing: border-box; }
  html, body { width: 902px; height: 1200px; overflow: hidden; background: var(--ink); }
  .flyer {
    position: relative; width: 902px; height: 1200px; overflow: hidden;
    background: var(--ink); color: var(--white);
    font-family: "Outfit", sans-serif;
  }
  .brand {
    position: absolute; left: 66px; top: 110px;
    display: flex; align-items: center; gap: 14px;
  }
  .brand-square { width: 38px; height: 38px; background: var(--green); }
  .brand-name {
    font-weight: 600; font-size: 22px; line-height: 1.2; color: var(--white);
    letter-spacing: 0.5px; width: 250px;
  }
  .headline {
    position: absolute; left: 64px; top: 252px;
    font-weight: 600; font-size: 72px; line-height: 76px; letter-spacing: -0.5px;
    white-space: nowrap;
  }
  .headline .small { font-size: 42px; }
  .headline .accent { color: var(--green); display: block; }
  .worker-photo {
    position: absolute; left: 505px; top: 65px; width: 397px; height: 410px;
  }
  .rule { position: absolute; height: 1.5px; background: var(--green); }
  .intro {
    position: absolute; left: 66px; top: 536px; width: 780px;
    font-weight: 500; font-size: 16.5px; line-height: 23.5px;
  }
  .services-title {
    position: absolute; left: 64px; top: 648px;
    font-weight: 600; font-size: 68px; line-height: 1; color: var(--green);
  }
  .service-list { position: absolute; list-style: none; font-weight: 500; font-size: 26px; }
  .service-list li { display: flex; align-items: center; gap: 14px; height: 33px; }
  .tick { width: 20px; height: 20px; flex: none; }
  .call {
    position: absolute; left: 64px; top: 912px;
    font-weight: 600; font-size: 44px; line-height: 40px; color: var(--green);
  }
  .phones {
    position: absolute; left: 66px; top: 1027px;
    font-weight: 500; font-size: 29px; line-height: 32px; letter-spacing: 1px;
  }
  .contact {
    position: absolute; left: 66px; top: 1122px; list-style: none;
    font-size: 13.5px; line-height: 24px; font-weight: 500;
  }
  .contact li { display: flex; align-items: center; gap: 5px; }
  .contact svg { width: 14px; height: 14px; }
  .social { position: absolute; left: 537px; top: 1124px; display: flex; gap: 10px; }
  .social span {
    width: 22px; height: 22px; border: 2.5px solid var(--green); border-radius: 50%;
  }
  .gallery { position: absolute; left: 420px; top: 805px; width: 482px; height: 395px; }
</style>
</head>
<body>
<main class="flyer">

  <div class="brand">
    <span class="brand-square"></span>
    <span class="brand-name">Halverton Construction And Masonry Ltd</span>
  </div>

  <svg class="worker-photo" viewBox="0 0 397 410" role="img" aria-label="Photo of a bricklayer in a hard hat laying a brick wall">
    <defs>
      <linearGradient id="workerTone" x1="0" y1="0" x2="1" y2="1">
        <stop offset="0" stop-color="#3fba68"/>
        <stop offset="0.55" stop-color="#7a6a5c"/>
        <stop offset="1" stop-color="#b86a4c"/>
      </linearGradient>
    </defs>
    <rect width="397" height="410" fill="url(#workerTone)"/>
  </svg>

  <h1 class="headline">
    Building <span class="small">and</span>
    <span class="accent">Brickwork</span>
    <span class="accent">Specialist’s</span>
  </h1>

  <div class="rule" style="left:54px; top:525px; width:793px;"></div>
  <p class="intro">Halverton Construction and Masonry offer the complete building service with over 15 years experience working throughout Cambridgeshire with local home owners looking to improve and add value to their properties.</p>
  <div class="rule" style="left:54px; top:616px; width:793px;"></div>

  <h2 class="services-title">SERVICES</h2>

  <ul class="service-list" style="left:66px; top:736px;">
    <li><svg class="tick" viewBox="0 0 20 20"><rect x="1.5" y="3.5" width="15" height="15" rx="2" fill="none" stroke="#3fba68" stroke-width="2"/><path d="M5 10.5l4 4 9-11" fill="none" stroke="#3fba68" stroke-width="2.4" stroke-linecap="round" stroke-linejoin="round"/></svg>New Builds</li>
    <li><svg class="tick" viewBox="0 0 20 20"><rect x="1.5" y="3.5" width="15" height="15" rx="2" fill="none" stroke="#3fba68" stroke-width="2"/><path d="M5 10.5l4 4 9-11" fill="none" stroke="#3fba68" stroke-width="2.4" stroke-linecap="round" stroke-linejoin="round"/></svg>Extensions</li>
    <li><svg class="tick" viewBox="0 0 20 20"><rect x="1.5" y="3.5" width="15" height="15" rx="2" fill="none" stroke="#3fba68" stroke-width="2"/><path d="M5 10.5l4 4 9-11" fill="none" stroke="#3fba68" stroke-width="2.4" stroke-linecap="round" stroke-linejoin="round"/></svg>Refurbishments</li>
  </ul>
  <ul class="service-list" style="left:455px; top:736px;">
    <li><svg class="tick" viewBox="0 0 20 20"><rect x="1.5" y="3.5" width="15" height="15" rx="2" fill="none" stroke="#3fba68" stroke-width="2"/><path d="M5 10.5l4 4 9-11" fill="none" stroke="#3fba68" stroke-width="2.4" stroke-linecap="round" stroke-linejoin="round"/></svg>Alterations</li>
    <li><svg class="tick" viewBox="0 0 20 20"><rect x="1.5" y="3.5" width="15" height="15" rx="2" fill="none" stroke="#3fba68" stroke-width="2"/><path d="M5 10.5l4 4 9-11" fill="none" stroke="#3fba68" stroke-width="2.4" stroke-linecap="round" stroke-linejoin="round"/></svg>Brickwork Specialists</li>
  </ul>

  <h2 class="call">CALL NOW<br>TODAY!</h2>
  <div class="rule" style="left:54px; top:1022px; width:259px;"></div>
  <p class="phones">01632 960481<br>0770 0900517</p>
  <div class="rule" style="left:54px; top:1098px; width:259px;"></div>

  <ul class="contact">
    <li><svg viewBox="0 0 14 14"><rect x="1" y="2.5" width="12" height="9" rx="1.5" fill="none" stroke="#3fba68" stroke-width="1.3"/><path d="M1.5 3.5l5.5 4 5.5-4" fill="none" stroke="#3fba68" stroke-width="1.3"/></svg>contact@halvertonconstructionandmasonry.co.uk</li>
    <li><svg viewBox="0 0 14 14"><circle cx="7" cy="7" r="5.8" fill="none" stroke="#3fba68" stroke-width="1.2"/><ellipse cx="7" cy="7" rx="2.6" ry="5.8" fill="none" stroke="#3fba68" stroke-width="1.1"/><path d="M1.2 7h11.6" stroke="#3fba68" stroke-width="1.1"/></svg>www.halvertonconstructionandmasonry.co.uk</li>
  </ul>

  <div class="social" aria-label="Social media links">
    <span></span><span></span>
  </div>

  <svg class="gallery" viewBox="0 0 482 395">
    <defs>
      <linearGradient id="roofTone" x1="0" y1="0" x2="0" y2="1">
        <stop offset="0" stop-color="#7fa6cf"/>
        <stop offset="0.35" stop-color="#c99a55"/>
        <stop offset="1" stop-color="#a8783d"/>
      </linearGradient>
      <linearGradient id="kitchenTone" x1="0" y1="0" x2="0" y2="1">
        <stop offset="0" stop-color="#dcdad6"/>
        <stop offset="0.6" stop-color="#8d8a84"/>
        <stop offset="1" stop-color="#6b5140"/>
      </linearGradient>
    </defs>
    <polygon points="215,190 482,168 482,395 190,395" fill="#3fba68"/>
    <polygon points="230,182 482,165 482,395 205,395" fill="url(#roofTone)" role="img" aria-label="Photo of new timber roof trusses under a blue sky"/>
    <polygon points="235,180 482,163 482,190 238,196" fill="#3fba68"/>
    <g transform="rotate(6 140 140)">
      <rect x="18" y="28" width="248" height="230" fill="#ffffff"/>
      <rect x="30" y="40" width="224" height="206" fill="url(#kitchenTone)" role="img" aria-label="Photo of a finished open-plan kitchen extension with roof lights"/>
    </g>
  </svg>

</main>
</body>
</html>
```